Cargo van wrap

The van I’m wrapping is a 2020 Brellick Roamer Van with a low roof and 130” wheelbase.

Already have a box truck wrap. I would like the van to use a similar design that fits the van.

Industry/Entity Type

Water damage restoration

Colors
0054AA
0677BA
7BADD7
CADEEF
E8F1F8

```html
<!DOCTYPE html>
<html lang="en">
<head>
<meta charset="utf-8">
<title>Harborline Restoration – Cargo Van Wrap</title>
<link rel="stylesheet" href="https://fonts.googleapis.com/css2?family=Oswald:wght@500;600&display=swap">
<style>
  :root {
    --blue: #0677BA;
    --blue-deep: #0054AA;
    --blue-mid: #7BADD7;
    --blue-pale: #CADEEF;
    --blue-mist: #E8F1F8;
    --panel-white: #F5F6F7;
    --graphite: #5F6062;
    --graphite-dark: #3A3B3D;
    --glass: #2E3033;
    --tyre: #1E1F21;
    --hub: #A7A9AC;
    --page: #FFFFFF;
  }
  html, body {
    margin: 0;
    width: 1200px;
    height: 1200px;
    overflow: hidden;
    background: var(--page);
  }
  .wrap-sheet { display: block; width: 1200px; height: 1200px; }
  .wrap-text { font-family: 'Oswald', 'Arial Narrow', sans-serif; font-weight: 600; }
  .brand-name { fill: var(--blue); font-size: 36px; letter-spacing: 0.5px; }
  .brand-name--large { font-size: 44px; }
  .phone { fill: var(--panel-white); font-size: 30px; letter-spacing: 3px; }
  .phone--graphite { fill: var(--graphite); font-size: 24px; letter-spacing: 1.5px; }
  .service-list { fill: var(--graphite); font-size: 17px; }
  .service-row { fill: var(--panel-white); font-size: 20px; letter-spacing: 1px; }
  .badge-number { fill: var(--blue-deep); font-size: 20px; font-style: italic; }
  .badge-label { fill: var(--blue-deep); font-size: 8px; font-weight: 500; }
  .body-panel { fill: var(--panel-white); }
  .skirt { fill: var(--graphite-dark); }
  .glass { fill: var(--glass); }
  .tyre { fill: var(--tyre); }
  .hub { fill: var(--hub); }
  .logo-ring { fill: none; stroke: var(--blue); stroke-width: 9; }
</style>
</head>
<body>
<svg class="wrap-sheet" viewBox="0 0 960 960" xmlns="http://www.w3.org/2000/svg">
  <defs>
    <path id="van-body" d="M62,112 Q62,98 80,98 L590,98 Q615,98 640,120 L800,215 Q830,232 870,240 L922,255 Q940,262 940,290 L940,364 Q940,376 928,376 L852,376 A62,62 0 0 0 728,376 L302,376 A62,62 0 0 0 178,376 L72,376 Q62,376 62,364 Z"/>
    <clipPath id="van-clip"><use href="#van-body"/></clipPath>
  </defs>

  <!-- Layout one: horizontal band -->
  <g class="van van--band">
    <use href="#van-body" class="body-panel"/>
    <g clip-path="url(#van-clip)">
      <rect class="skirt" x="40" y="326" width="920" height="60"/>
      <rect fill="var(--blue)" x="320" y="352" width="395" height="12"/>
      <polygon fill="var(--graphite)" points="62,222 585,222 648,322 636,322 577,230 62,230"/>
      <polygon fill="var(--blue)" points="62,244 572,244 622,322 62,322"/>
      <polygon class="glass" points="612,112 640,122 790,212 790,246 612,246"/>
      <polygon class="glass" points="872,248 925,262 930,286 880,280"/>
    </g>
    <circle class="logo-ring" cx="135" cy="165" r="44"/>
    <text class="wrap-text brand-name" x="196" y="192">HARBORLINE RESTORATION</text>
    <text class="wrap-text phone" x="198" y="286">(702)555-0148</text>
    <g class="wrap-text service-list">
      <text x="654" y="271">• WATER</text>
      <text x="654" y="293">• FIRE</text>
      <text x="654" y="315">• MOLD</text>
    </g>
    <g class="service-badge">
      <circle cx="808" cy="282" r="14" fill="none" stroke="var(--blue-mid)" stroke-width="2"/>
      <text class="wrap-text badge-number" x="788" y="290">24</text>
      <text class="wrap-text badge-label" x="824" y="283">Hours</text>
      <text class="wrap-text badge-label" x="824" y="293">Services</text>
    </g>
    <circle class="tyre" cx="240" cy="384" r="54"/><circle class="hub" cx="240" cy="384" r="26"/>
    <circle class="tyre" cx="790" cy="384" r="54"/><circle class="hub" cx="790" cy="384" r="26"/>
  </g>

  <!-- Layout two: diagonal sweep -->
  <g class="van van--sweep" transform="translate(0,440)">
    <use href="#van-body" class="body-panel"/>
    <g clip-path="url(#van-clip)">
      <polygon fill="var(--graphite)" points="40,90 960,90 960,250 780,225 80,120 40,120"/>
      <polygon fill="var(--panel-white)" points="92,112 780,216 780,222 92,118"/>
      <polygon fill="var(--blue)" points="62,222 200,268 712,340 712,360 62,360"/>
      <rect class="skirt" x="40" y="326" width="920" height="60"/>
      <rect fill="var(--blue)" x="320" y="352" width="395" height="12"/>
      <polygon class="glass" points="612,112 640,122 790,212 790,236 612,236"/>
      <polygon class="glass" points="872,248 925,262 930,286 880,280"/>
    </g>
    <circle class="logo-ring" cx="180" cy="180" r="60"/>
    <text class="wrap-text service-row" x="340" y="142" transform="rotate(8.6 340 142)">• WATER • FIRE • MOLD</text>
    <text class="wrap-text brand-name brand-name--large" x="262" y="226" transform="rotate(8.6 262 226)">HARBORLINE RESTORATION</text>
    <text class="wrap-text phone--graphite" x="232" y="262" transform="rotate(8.6 232 262)">(702)555-0148</text>
    <g class="service-badge">
      <circle cx="808" cy="282" r="14" fill="none" stroke="var(--blue-mid)" stroke-width="2"/>
      <text class="wrap-text badge-number" x="788" y="290">24</text>
      <text class="wrap-text badge-label" x="824" y="283">Hours</text>
      <text class="wrap-text badge-label" x="824" y="293">Services</text>
    </g>
    <circle class="tyre" cx="240" cy="384" r="54"/><circle class="hub" cx="240" cy="384" r="26"/>
    <circle class="tyre" cx="790" cy="384" r="54"/><circle class="hub" cx="790" cy="384" r="26"/>
  </g>
</svg>
</body>
</html>
```